A billboard for Harlow Ridge Construction size 36.5’ x 14.5’

Hi guys. We are purchasing a billboard and are looking for a design (size 36.5’ x 14.5’). Our slogan is "Quality you deserve, service you can count on". The goal of this billboard is brand recognition primarily letting people know we do roofs. Attached are logos that can be used if needed. Not necessarily all of them need to be used.

Target Market(s)

Residents in the local areas needing or thinking about a roof replacement

Industry/Entity Type

Roofing

Requirements
Must have
• Logo and services (roof replacement, gutters, siding, and snow removal)
Nice to have
• take a look at our website for ideas www.harlowridgeconstruction.example

```html
<!DOCTYPE html>
<html lang="en">
<head>
<meta charset="utf-8">
<title>Harlow Ridge Construction Billboard</title>
<link rel="stylesheet" href="https://fonts.googleapis.com/css2?family=Montserrat:wght@500;600;700;800&display=swap">
<style>
  :root {
    --red: #ea1f25;
    --red-deep: #b8181e;
    --charcoal: #2d2d2f;
    --ink: #1f1f21;
    --white: #ffffff;
    --stage: #e8eaee;
    --badge-blue: #1f6f93;
    --badge-grey: #9b9ea3;
  }
  html, body {
    margin: 0;
    padding: 0;
    width: 1200px;
    height: 779px;
    overflow: hidden;
    background: var(--stage);
  }
  .billboard {
    position: absolute;
    left: 0;
    top: 178px;
    width: 1200px;
    height: 423px;
    display: block;
  }
  .headline { font-family: "Montserrat", sans-serif; font-weight: 800; }
  .service { font-family: "Montserrat", sans-serif; font-weight: 600; fill: var(--white); }
  .brand-name { font-family: "Montserrat", sans-serif; font-weight: 700; fill: var(--ink); }
  .cta-label { font-family: "Montserrat", sans-serif; font-weight: 500; fill: var(--ink); }
  .cta-phone { font-family: "Montserrat", sans-serif; font-weight: 800; fill: var(--red); }
</style>
</head>
<body>
<svg class="billboard" viewBox="0 0 1290 455" xmlns="http://www.w3.org/2000/svg" aria-label="Harlow Ridge Construction billboard">
  <defs>
    <linearGradient id="houseTones" x1="0" y1="0" x2="0" y2="1">
      <stop offset="0" stop-color="#5f7c4a"/>
      <stop offset="0.35" stop-color="#7d7168"/>
      <stop offset="0.7" stop-color="#c9b79c"/>
      <stop offset="1" stop-color="#8a7a68"/>
    </linearGradient>
  </defs>

  <!-- base -->
  <rect class="panel-base" x="0" y="0" width="1290" height="455" fill="var(--white)"/>

  <!-- right dark frame -->
  <polygon class="frame-dark" points="800,0 1290,0 1290,455 800,455 650,227" fill="var(--charcoal)"/>
  <polygon class="frame-white" points="790,35 1290,35 1290,425 790,425 664,227" fill="var(--white)"/>
  <polygon class="house-photo" role="img" aria-label="Photo of a two-storey house with a new shingle roof" points="802,50 1287,50 1287,410 802,410 676,227" fill="url(#houseTones)"/>

  <!-- chevrons -->
  <polygon class="accent-triangle" points="592,17 682,17 647,112" fill="var(--red-deep)"/>
  <polygon class="chevron" points="722,17 797,17 662,227 797,442 737,442 587,227" fill="var(--red)"/>

  <!-- top-left corner -->
  <polygon class="corner-accent" points="0,0 42,0 112,114 0,114" fill="var(--red)"/>

  <!-- brand -->
  <rect class="brand-square" x="186" y="50" width="16" height="16" fill="var(--red)"/>
  <text class="brand-name" x="214" y="66" font-size="24" textLength="250" lengthAdjust="spacingAndGlyphs">Harlow Ridge</text>
  <text class="brand-name" x="214" y="94" font-size="20" textLength="180" lengthAdjust="spacingAndGlyphs">Construction</text>

  <!-- slogan band -->
  <polygon class="slogan-band" points="0,114 652,114 578,228 668,372 0,372" fill="var(--charcoal)"/>
  <text class="headline" x="43" y="172" font-size="46" fill="var(--white)" textLength="382" lengthAdjust="spacingAndGlyphs">QUALITY YOU</text>
  <text class="headline" x="43" y="223" font-size="48" fill="var(--red)" textLength="510" lengthAdjust="spacingAndGlyphs">DESERVE SERVICE</text>
  <text class="headline" x="43" y="264" font-size="36" fill="var(--white)" textLength="454" lengthAdjust="spacingAndGlyphs">YOU CAN COUNT ON</text>

  <!-- services band -->
  <polygon class="services-band" points="0,283 612,283 642,360 0,360" fill="var(--red)"/>
  <g class="tick-box" fill="none" stroke="var(--white)" stroke-width="2.5">
    <rect x="51" y="294" width="20" height="20"/>
    <rect x="384" y="294" width="20" height="20"/>
    <rect x="51" y="328" width="20" height="20"/>
    <rect x="200" y="328" width="20" height="20"/>
    <path d="M54 302 l6 7 l13 -15"/>
    <path d="M387 302 l6 7 l13 -15"/>
    <path d="M54 336 l6 7 l13 -15"/>
    <path d="M203 336 l6 7 l13 -15"/>
  </g>
  <text class="service" x="80" y="313" font-size="22" textLength="272" lengthAdjust="spacingAndGlyphs">ROOF REPLACEMENT</text>
  <text class="service" x="413" y="313" font-size="22" textLength="117" lengthAdjust="spacingAndGlyphs">GUTTERS</text>
  <text class="service" x="80" y="347" font-size="22" textLength="88" lengthAdjust="spacingAndGlyphs">SIDING</text>
  <text class="service" x="230" y="347" font-size="22" textLength="216" lengthAdjust="spacingAndGlyphs">SNOW REMOVAL</text>

  <!-- call to action -->
  <rect class="phone-icon-box" x="40" y="388" width="52" height="48" rx="9" fill="var(--charcoal)"/>
  <circle cx="66" cy="412" r="17" fill="none" stroke="var(--white)" stroke-width="3"/>
  <path class="phone-handset" d="M58 403 q-4 4 2 12 q6 8 11 6 l2 -3 l-5 -4 l-2 2 q-4 -2 -6 -7 l2 -2 l-3 -5 z" fill="var(--white)"/>
  <text class="cta-label" x="102" y="404" font-size="18" textLength="234" lengthAdjust="spacingAndGlyphs">CALL FOR APPOINTMENT</text>
  <text class="cta-phone" x="102" y="432" font-size="28" textLength="235" lengthAdjust="spacingAndGlyphs">555-013-4827</text>

  <!-- partner badges -->
  <circle class="partner-badge" cx="412" cy="410" r="20" fill="var(--badge-grey)"/>
  <rect class="partner-badge" x="472" y="390" width="125" height="42" rx="3" fill="var(--badge-blue)"/>
  <rect class="partner-badge" x="620" y="390" width="38" height="38" rx="3" fill="var(--badge-grey)" opacity="0.6"/>
</svg>
</body>
</html>
```